Upscale Adult website

Looking for the design mock-up of an intuitive, professional and upscale adult website. No HTML necessary, just a competent design theme. The site will be category centric. This means that finding and selecting a specific categories in any easy and intuitive way is vey important. Looking for mock-up of Home Page, a Category Screen, and the Login Screen. The site should have a fun feel but be more corporate rather than "porn." There must also be free space where ads will appear. See attached file for complete list of functionality and necessary icons for the Home Screen.

Industry/Entity Type

Adult

```html
<!DOCTYPE html>
<html lang="en">
<head>
<meta charset="utf-8">
<title>Velvet Reel – Home</title>
<link rel="stylesheet" href="https://fonts.googleapis.com/css2?family=Roboto+Condensed:wght@400;500;700&family=Ubuntu:wght@400;500;700&display=swap">
<style>
:root{
  --page:#dfe4e5;
  --teal:#2bb3a2;
  --teal-dark:#1e8c7f;
  --teal-ink:#1c7466;
  --panel:#eef3f2;
  --panel-edge:#ffffff;
  --title-red:#d3202a;
  --heart:#e0323c;
  --ink:#3b3b3b;
  --muted:#b9c4c4;
  --footer-link:#7a2c2c;
  --label-faint:#d2d6d6;
}
*{box-sizing:border-box;margin:0;padding:0}
html,body{width:902px;height:1200px;overflow:hidden}
body{background:var(--page);font-family:"Ubuntu",sans-serif;position:relative;color:var(--ink)}
.abs{position:absolute}

/* top bar */
.topbar{left:0;top:0;width:902px;height:34px;background:var(--teal);box-shadow:0 2px 4px rgba(0,0,0,.15)}
.brand{left:100px;top:0;width:76px;height:34px;background:var(--teal-dark);color:#fff;font:500 12px "Ubuntu",sans-serif;display:flex;align-items:center;justify-content:center;white-space:nowrap}
.main-nav{left:194px;top:0;width:388px;height:34px;display:flex;justify-content:space-between;align-items:center;white-space:nowrap}
.main-nav a{color:#fff;text-decoration:none;font:500 12px "Roboto Condensed",sans-serif}
.nav-icon{top:7px;width:20px;height:20px}
.field{top:9px;height:14px;border-radius:7px;background:var(--teal-dark);color:#fff;font:9px "Ubuntu",sans-serif;padding-left:9px;line-height:14px}
.field-go{right:5px;top:0;font-size:10px}
.register{left:776px;top:22px;color:#fff;font:7px "Ubuntu",sans-serif}

/* categories */
.category{top:46px;width:92px;height:93px;background:#fff;border:1px solid #c9d0d0;padding:3px}
.category-art{width:100%;height:100%;position:relative;background:linear-gradient(135deg,#d9b49c,#8c6a58 60%,#f0ece8)}
.category-art.dark{background:linear-gradient(135deg,#2a2a2a,#050505)}
.category-art.blue{background:linear-gradient(160deg,#5d8ec9,#d99070 60%,#2a2a2a)}
.category-art.light{background:linear-gradient(135deg,#f2ebe6,#c89a80 55%,#efe6e0)}
.category-label{position:absolute;left:0;right:0;bottom:3px;height:16px;background:rgba(255,255,255,.85);color:var(--teal-ink);font:700 8px "Ubuntu",sans-serif;text-align:center;line-height:16px}

/* banner */
.banner{left:97px;top:150px;width:706px;height:175px;background:linear-gradient(180deg,#fafafa,#e6eaea);border:2px solid #fff;box-shadow:0 1px 3px rgba(0,0,0,.2)}
.banner-label{left:12px;top:12px;color:var(--label-faint);font:700 11px "Ubuntu",sans-serif;white-space:nowrap;z-index:1}
.banner-models{left:245px;top:12px;width:345px;height:161px;background:linear-gradient(90deg,#e8c9ae,#f2d9c4 30%,#d9a88e 50%,#efd3bd 70%,#c99b80);border-radius:4px 4px 0 0}
.banner-dots{right:12px;bottom:10px;display:flex;gap:2px}
.banner-dots span{width:8px;height:8px;border-radius:50%;background:#7fc9bd;border:1px solid #5aa99c}
.banner-dots span:first-child{background:var(--teal-dark)}

/* panels */
.panel{background:var(--panel);border:2px solid var(--panel-edge);box-shadow:0 1px 4px rgba(0,0,0,.18)}
.panel-title{position:absolute;left:16px;top:10px;color:var(--teal-ink);font:500 12px "Roboto Condensed",sans-serif;text-transform:uppercase;white-space:nowrap}

/* video cards */
.video{width:122px}
.thumb{width:114px;height:114px;border:2px solid #5b5b5b;position:relative;background:linear-gradient(135deg,#e2c4ad,#8d6a55 55%,#ede9e6)}
.thumb.dark{background:linear-gradient(135deg,#2b2b2b,#000)}
.thumb.blue{background:linear-gradient(160deg,#6a97c9,#c98e72 55%,#f2f0ee)}
.thumb.light{background:linear-gradient(135deg,#f3ede8,#c9a088 55%,#e9e2dc)}
.thumb svg{position:absolute;left:44px;top:42px}
.video-title{margin-top:6px;color:var(--title-red);font:12px/14px "Roboto Condensed",sans-serif;white-space:nowrap}
.video-meta{display:flex;justify-content:space-between;align-items:center;font:11px "Roboto Condensed",sans-serif;color:var(--ink);width:114px;white-space:nowrap}
.likes{display:flex;align-items:center;gap:3px}

/* pagination */
.pager{display:flex;gap:7px;align-items:center}
.pager span{width:16px;height:16px;border-radius:50%;border:1px solid var(--muted);color:var(--muted);font:9px/14px "Ubuntu",sans-serif;text-align:center}
.pager span.current{border-color:var(--teal-ink);color:var(--teal-ink);font-weight:700}
.pager .gap{border:none;width:6px}

/* footer */
.footer{left:0;top:1075px;width:902px;height:125px;background:var(--teal)}
.footer-col{top:14px;font:12px "Roboto Condensed",sans-serif}
.footer-col h4{color:#fff;font:500 12px "Roboto Condensed",sans-serif;text-transform:uppercase;margin-bottom:4px;white-space:nowrap}
.footer-col a{display:block;color:var(--footer-link);text-decoration:none;line-height:14.5px;padding-left:14px;white-space:nowrap}
.copyright{left:0;width:902px;top:1183px;text-align:center;color:#155f55;font:7px "Ubuntu",sans-serif}
</style>
</head>
<body>

<header class="abs topbar">
  <div class="abs brand">YOUR LOGO</div>
  <nav class="abs main-nav">
    <a href="#">HOME</a><a href="#">HIGHEST RATED</a><a href="#">MOST VIEWED</a><a href="#">RECENTLY ADDED</a><a href="#">CATEGORIES</a>
  </nav>
  <svg class="abs nav-icon" style="left:593px" viewBox="0 0 20 20"><circle cx="10" cy="10" r="8.5" fill="none" stroke="#fff" stroke-width="1.5"/><path d="M10 14.5 5.8 10.4a2.4 2.4 0 0 1 4.2-2.6 2.4 2.4 0 0 1 4.2 2.6Z" fill="#fff"/></svg>
  <svg class="abs nav-icon" style="left:620px" viewBox="0 0 20 20"><circle cx="10" cy="10" r="8.5" fill="none" stroke="#fff" stroke-width="1.5"/><path d="M10 5v9M7 7h6M6.5 11.5a3.5 3 0 0 0 7 0" fill="none" stroke="#fff" stroke-width="1.4"/></svg>
  <div class="abs field" style="left:654px;width:70px">name</div>
  <div class="abs field" style="left:732px;width:70px">password<span class="abs field-go">&gt;</span></div>
  <div class="abs register">or register</div>
</header>

<section class="categories">
  <div class="abs category" style="left:97px"><div class="category-art" role="img" aria-label="Category preview photo"><span class="category-label">CATEGORY 1.</span></div></div>
  <div class="abs category" style="left:199px"><div class="category-art dark" role="img" aria-label="Category preview photo"><span class="category-label">CATEGORY 1.</span></div></div>
  <div class="abs category" style="left:301px"><div class="category-art light" role="img" aria-label="Category preview photo"><span class="category-label">CATEGORY 1.</span></div></div>
  <div class="abs category" style="left:403px"><div class="category-art blue" role="img" aria-label="Category preview photo"><span class="category-label">CATEGORY 1.</span></div></div>
  <div class="abs category" style="left:505px"><div class="category-art" role="img" aria-label="Category preview photo"><span class="category-label">CATEGORY 1.</span></div></div>
  <div class="abs category" style="left:607px"><div class="category-art blue" role="img" aria-label="Category preview photo"><span class="category-label">CATEGORY 1.</span></div></div>
  <div class="abs category" style="left:709px"><div class="category-art" role="img" aria-label="Category preview photo"><span class="category-label">CATEGORY 1.</span></div></div>
</section>

<section class="abs banner">
  <div class="abs banner-label">FEATURED VIDEOS/ADS AND BANNERS</div>
  <div class="abs banner-models" role="img" aria-label="Featured banner photo of five models in lingerie"></div>
  <div class="abs banner-dots"><span></span><span></span><span></span><span></span><span></span></div>
</section>

<svg width="0" height="0" style="position:absolute">
  <defs>
    <symbol id="play" viewBox="0 0 24 26"><path d="M2 1 23 13 2 25Z" fill="#fff"/></symbol>
    <symbol id="heart" viewBox="0 0 12 12"><circle cx="6" cy="6" r="5.3" fill="none" stroke="#e0323c" stroke-width="1.1"/><path d="M6 8.8 3.4 6.2a1.5 1.5 0 0 1 2.6-1.6 1.5 1.5 0 0 1 2.6 1.6Z" fill="#e0323c"/></symbol>
  </defs>
</svg>

<section class="abs panel" style="left:97px;top:344px;width:285px;height:442px">
  <h2 class="panel-title">Recently added videos</h2>
  <div class="abs video" style="left:22px;top:33px"><div class="thumb" role="img" aria-label="Video still of a couple"><svg width="24" height="26"><use href="#play"/></svg></div><p class="video-title">Title of the video first<br>and second line...</p><div class="video-meta"><span>200 views</span><span class="likes"><svg width="12" height="12"><use href="#heart"/></svg>&nbsp;&nbsp;15</span></div></div>
  <div class="abs video" style="left:146px;top:33px"><div class="thumb dark" role="img" aria-label="Dark video still"><svg width="24" height="26"><use href="#play"/></svg></div><p class="video-title">Title of the video first<br>and second line...</p><div class="video-meta"><span>5.003 views</span><span class="likes"><svg width="12" height="12"><use href="#heart"/></svg>243</span></div></div>
  <div class="abs video" style="left:22px;top:210px"><div class="thumb" role="img" aria-label="Video still of a couple"><svg width="24" height="26"><use href="#play"/></svg></div><p class="video-title">Title of the video first<br>and second line...</p><div class="video-meta"><span>200 views</span><span class="likes"><svg width="12" height="12"><use href="#heart"/></svg>&nbsp;&nbsp;15</span></div></div>
  <div class="abs video" style="left:146px;top:210px"><div class="thumb dark" role="img" aria-label="Dark video still"><svg width="24" height="26"><use href="#play"/></svg></div><p class="video-title">Title of the video first<br>and second line...</p><div class="video-meta"><span>5.003 views</span><span class="likes"><svg width="12" height="12"><use href="#heart"/></svg>243</span></div></div>
  <div class="abs pager" style="left:24px;top:404px"><span class="current">1</span><span>2</span><span>3</span><span>4</span><span>5</span><span>6</span><span>7</span><span class="gap">...</span><span>9</span><span>&#9656;</span></div>
</section>

<section class="abs panel" style="left:395px;top:344px;width:408px;height:442px">
  <h2 class="panel-title">Most viewed videos</h2>
  <div class="abs video" style="left:20px;top:33px"><div class="thumb light" role="img" aria-label="Video still of a couple"><svg width="24" height="26"><use href="#play"/></svg></div><p class="video-title">Title of the video first<br>and second line...</p><div class="video-meta"><span>1.233 views</span><span class="likes"><svg width="12" height="12"><use href="#heart"/></svg>175</span></div></div>
  <div class="abs video" style="left:145px;top:33px"><div class="thumb blue" role="img" aria-label="Video still of a model at the beach"><svg width="24" height="26"><use href="#play"/></svg></div><p class="video-title">Title of the video first<br>and second line...</p><div class="video-meta"><span>1.233.989 views</span><span class="likes"><svg width="12" height="12"><use href="#heart"/></svg>243</span></div></div>
  <div class="abs video" style="left:270px;top:33px"><div class="thumb" role="img" aria-label="Video still of a couple"><svg width="24" height="26"><use href="#play"/></svg></div><p class="video-title">Title of the video first<br>and second line...</p><div class="video-meta"><span>33.989 views</span><span class="likes"><svg width="12" height="12"><use href="#heart"/></svg>175</span></div></div>
  <div class="abs video" style="left:20px;top:210px"><div class="thumb light" role="img" aria-label="Video still of a couple"><svg width="24" height="26"><use href="#play"/></svg></div><p class="video-title">Title of the video first<br>and second line...</p><div class="video-meta"><span>1.233 views</span><span class="likes"><svg width="12" height="12"><use href="#heart"/></svg>175</span></div></div>
  <div class="abs video" style="left:145px;top:210px"><div class="thumb blue" role="img" aria-label="Video still of a model at the beach"><svg width="24" height="26"><use href="#play"/></svg></div><p class="video-title">Title of the video first<br>and second line...</p><div class="video-meta"><span>1.233.989 views</span><span class="likes"><svg width="12" height="12"><use href="#heart"/></svg>243</span></div></div>
  <div class="abs video" style="left:270px;top:210px"><div class="thumb" role="img" aria-label="Video still of a couple"><svg width="24" height="26"><use href="#play"/></svg></div><p class="video-title">Title of the video first<br>and second line...</p><div class="video-meta"><span>33.989 views</span><span class="likes"><svg width="12" height="12"><use href="#heart"/></svg>175</span></div></div>
  <div class="abs pager" style="left:84px;top:404px"><span class="current">1</span><span>2</span><span>3</span><span>4</span><span>5</span><span>6</span><span>7</span><span class="gap">...</span><span>9</span><span>&#9656;</span></div>
</section>

<section class="abs panel" style="left:97px;top:809px;width:706px;height:210px">
  <h2 class="panel-title">Featured videos</h2>
  <div class="abs video" style="left:44px;top:33px"><div class="thumb" role="img" aria-label="Video still of a couple"><svg width="24" height="26"><use href="#play"/></svg></div><p class="video-title">Title of the video first<br>and second line...</p><div class="video-meta"><span>200 views</span><span class="likes"><svg width="12" height="12"><use href="#heart"/></svg>&nbsp;&nbsp;15</span></div></div>
  <div class="abs video" style="left:169px;top:33px"><div class="thumb dark" role="img" aria-label="Dark video still"><svg width="24" height="26"><use href="#play"/></svg></div><p class="video-title">Title of the video first<br>and second line...</p><div class="video-meta"><span>5.003 views</span><span class="likes"><svg width="12" height="12"><use href="#heart"/></svg>243</span></div></div>
  <div class="abs video" style="left:295px;top:33px"><div class="thumb light" role="img" aria-label="Video still of a couple"><svg width="24" height="26"><use href="#play"/></svg></div><p class="video-title">Title of the video first<br>and second line...</p><div class="video-meta"><span>1.233 views</span><span class="likes"><svg width="12" height="12"><use href="#heart"/></svg>175</span></div></div>
  <div class="abs video" style="left:420px;top:33px"><div class="thumb blue" role="img" aria-label="Video still of a model at the beach"><svg width="24" height="26"><use href="#play"/></svg></div><p class="video-title">Title of the video first<br>and second line...</p><div class="video-meta"><span>1.233.989 views</span><span class="likes"><svg width="12" height="12"><use href="#heart"/></svg>243</span></div></div>
  <div class="abs video" style="left:546px;top:33px"><div class="thumb" role="img" aria-label="Video still of a couple"><svg width="24" height="26"><use href="#play"/></svg></div><p class="video-title">Title of the video first<br>and second line...</p><div class="video-meta"><span>33.989 views</span><span class="likes"><svg width="12" height="12"><use href="#heart"/></svg>175</span></div></div>
  <svg class="abs" style="left:14px;top:86px" width="14" height="28" viewBox="0 0 14 28"><path d="M13 1 1 14 13 27Z" fill="#fff"/></svg>
  <svg class="abs" style="left:674px;top:86px" width="14" height="28" viewBox="0 0 14 28"><path d="M1 1 13 14 1 27Z" fill="#fff"/></svg>
</section>

<footer class="abs footer">
  <div class="abs footer-col" style="left:98px"><h4>Information</h4><a href="#">information</a><a href="#">information</a><a href="#">information</a><a href="#">information</a></div>
  <div class="abs footer-col" style="left:257px"><h4>Support</h4><a href="#">support</a><a href="#">support</a><a href="#">support</a><a href="#">support</a></div>
  <div class="abs footer-col" style="left:414px"><h4>Our team</h4><a href="#">ourteam</a><a href="#">ourteam</a><a href="#">ourteam</a><a href="#">ourteam</a></div>
  <div class="abs footer-col" style="left:572px"><h4>Other menu</h4><a href="#">other menu</a><a href="#">other menu</a><a href="#">other menu</a><a href="#">other menu</a></div>
  <div class="abs footer-col" style="left:732px"><h4>Other menu</h4><a href="#">other menu</a><a href="#">other menu</a><a href="#">other menu</a><a href="#">other menu</a></div>
</footer>
<div class="abs copyright">© VELVETREEL.EXAMPLE, 2014</div>

</body>
</html>
```